Start-up Cleaning Business Needs Professional Business Cards

Marisol's Butler Tidying, LLC, is a start-up business based in the Northern Virginia suburbs of Washington, DC. MBT provides cleaning and housekeeping services for homes and offices. We have three core values:

1. We are personal. We value knowing and being known by our customers and each other. If you want nameless, faceless service, you should choose another provider. We put "personal" at the front of the list, because it is most important to us; the design we choose will convey this value.

2. Like a hotel concierge, we are professional in attitude, posture, communication and processes.

3. Like a hotel concierge, we solve problems with a can-do attitude and never make excuses.

Our uniforms are khaki pants with pink polo shirts.

Our logo is attached. There are other symbols, not represented in our logo, that may convey our values well, such as a top hat and bow tie, magnifying glass, desk bell, etc.

Please include fields for an individual's name and title, office phone number, mobile phone number, email address and website address (www.marisolsbutlertidying-example.com).

Standard U.S. size: 2" x 3.5"
Updates

I should have mentioned that the purpose of all our advertising - business cards included - is to motivate potential customers to call or email to arrange a free in-home estimate.

```html
<!DOCTYPE html>
<html lang="en">
<head>
<meta charset="utf-8">
<title>Marisol's Butler Tidying – Business Card</title>
<link href="https://fonts.googleapis.com/css2?family=Arimo:wght@400;700&display=swap" rel="stylesheet">
<style>
  :root {
    --backdrop: #efebe5;
    --card-white: #ffffff;
    --brand-pink: #ec3d96;
    --ink-dark: #3a3a3a;
    --rule-dark: #2e2e2e;
    --stripe-gray: #cfcfcf;
    --blush: #f6c6de;
    --text-on-pink: #ffffff;
  }
  * { margin: 0; padding: 0; box-sizing: border-box; }
  html, body {
    width: 1050px; height: 1200px; overflow: hidden;
    background: var(--backdrop);
    font-family: "Arimo", Arial, sans-serif;
  }
  .canvas { position: relative; width: 1050px; height: 1200px; }

  .card {
    position: absolute;
    background: var(--card-white);
    box-shadow: 0 2px 8px rgba(0,0,0,0.15);
    overflow: hidden;
  }
  .card--front { left: 61px; top: 49px; width: 916px; height: 525px; }
  .card--back  { left: 79px; top: 612px; width: 919px; height: 526px; }

  .edge-stripes { position: absolute; left: 0; top: 0; width: 20px; height: 525px; }

  .brand-panel {
    position: absolute; left: 20px; top: 0; width: 391px; height: 525px;
    display: flex; flex-direction: column; align-items: center; justify-content: center;
  }
  .brand-dot {
    width: 150px; height: 150px; border-radius: 50%;
    background: var(--blush); margin-bottom: 38px;
  }
  .brand-name {
    color: var(--ink-dark); font-weight: 400; text-align: center;
    line-height: 1.15;
  }
  .brand-name .line-main { display: block; font-size: 50px; }
  .brand-name .line-sub { display: block; font-size: 22px; letter-spacing: 1px; }

  .divider {
    position: absolute; left: 411px; top: 0; width: 5px; height: 525px;
    background: var(--rule-dark);
  }

  .info-panel {
    position: absolute; left: 421px; top: 0; right: 0; height: 525px;
    background: var(--brand-pink); color: var(--text-on-pink);
    padding: 38px 0 0 30px;
  }
  .person-name { font-size: 33px; font-weight: 700; line-height: 1.2; }
  .person-title { font-size: 21px; margin-top: 6px; }

  .contact-list { list-style: none; margin-top: 50px; }
  .contact-list li {
    display: flex; align-items: center; font-size: 21px; height: 36px;
  }
  .contact-list svg { width: 18px; height: 18px; margin-right: 7px; flex: none; }

  .cta { margin-top: 42px; font-size: 35px; line-height: 1.32; }
  .cta strong { font-weight: 700; display: block; }

  .back-logo {
    position: absolute; left: 0; right: 0; top: 0; bottom: 0;
    display: flex; align-items: center; justify-content: center;
  }
  .back-name {
    color: var(--ink-dark); font-size: 46px; font-weight: 400; letter-spacing: 1px;
  }
</style>
</head>
<body>
<div class="canvas">

  <section class="card card--front">
    <svg class="edge-stripes" viewBox="0 0 20 525" aria-hidden="true">
      <polygon points="0,0 20,0 20,120 0,150" fill="#3f3f3f"/>
      <polygon points="0,150 20,120 20,185 0,215" fill="var(--stripe-gray)"/>
      <polygon points="0,215 20,185 20,400 0,430" fill="var(--brand-pink)"/>
      <polygon points="0,430 20,400 20,525 0,525" fill="var(--stripe-gray)"/>
    </svg>

    <div class="brand-panel">
      <div class="brand-dot"></div>
      <div class="brand-name">
        <span class="line-main">Marisol's</span>
        <span class="line-sub">Butler Tidying</span>
      </div>
    </div>

    <div class="divider"></div>

    <div class="info-panel">
      <div class="person-name">Individuals name</div>
      <div class="person-title">Title</div>

      <ul class="contact-list">
        <li>
          <svg viewBox="0 0 20 20" aria-hidden="true"><circle cx="10" cy="10" r="8.5" fill="none" stroke="#fff" stroke-width="1.5"/><path d="M6.5 5.5l2 0 .8 2.4-1.2 1a6 6 0 0 0 3 3l1-1.2 2.4.8v2a1 1 0 0 1-1 1A8 8 0 0 1 5.5 6.5a1 1 0 0 1 1-1z" fill="#fff"/></svg>
          (123) 456-7890
        </li>
        <li>
          <svg viewBox="0 0 20 20" aria-hidden="true"><rect x="6" y="2" width="8" height="16" rx="1.5" fill="#fff"/><rect x="7.5" y="4" width="5" height="9" fill="var(--brand-pink)"/></svg>
          (123) 456-7890
        </li>
        <li>
          <svg viewBox="0 0 20 20" aria-hidden="true"><rect x="2" y="5" width="16" height="11" fill="#fff"/><path d="M2 5l8 6 8-6" fill="none" stroke="var(--brand-pink)" stroke-width="1.4"/></svg>
          info@marisolsbutlertidying-example.com
        </li>
        <li>
          <svg viewBox="0 0 20 20" aria-hidden="true"><circle cx="10" cy="10" r="8" fill="none" stroke="#fff" stroke-width="1.5"/><ellipse cx="10" cy="10" rx="3.5" ry="8" fill="none" stroke="#fff" stroke-width="1.3"/><line x1="2" y1="10" x2="18" y2="10" stroke="#fff" stroke-width="1.3"/></svg>
          www.marisolsbutlertidying-example.com
        </li>
      </ul>

      <p class="cta"><strong>Call or email</strong>to arrange a free in<br>home estimate</p>
    </div>
  </section>

  <section class="card card--back">
    <div class="back-logo">
      <span class="back-name">Marisol's Butler Tidying, LLC</span>
    </div>
  </section>

</div>
</body>
</html>
```